Corporate brochure design 4 pages

Hi,

We are a real estate company based in Europe.

We have almost finalized a rebranding.

We are developing a brand book guidelines (still on working process) to help you undertstand the look and feel of our new CI. I would like to receive proposals of design for a corporate brochure template. I need to receive the Indesign files with full ownership rights to be able to adapt all our documentation with this template.
Regarding the images, you can take gabaris on www.pelvaromedia.com. I will be able to take them afterwards.

There will be 4 pages. you will receive the 4 pages on pdf for your consideration with our (almost) actual layout.

- 1st page: cover
- 2nd page: company presentation in french and english
- 3rd page: some market data + graph
- 4th page: 2 retail centers presentation.

In the template, i need to have:
- the paragraph styles in order
- 2 different masters with top/bottom/page number aso.

Please feel free to ask any other questions.

best regards,
Updates

I would like to precise tha t we are active on the commercial real estate sector:

- office transactions (rent /sales)
- property management of administrative and business buildings
- Valuation of properties
- Capital markets (investment advices for selling building)

Industry/Entity Type

Real Estate

Colors

Designer to choose colors to be used in the design.

```html
<!DOCTYPE html>
<html lang="en">
<head>
<meta charset="utf-8">
<title>Brochure Cover – Office Market Report</title>
<link rel="stylesheet" href="https://fonts.googleapis.com/css2?family=Kreon:wght@400;700&family=Roboto:wght@300;400;900&display=swap">
<style>
  :root {
    --board: #161616;
    --accent-text: #e8692a;
    --cover-orange: #f26a21;
    --white: #ffffff;
    --photo-light: #e9e6df;
    --photo-mid: #c9c3b6;
    --photo-dark: #8c877d;
  }
  * { box-sizing: border-box; margin: 0; padding: 0; }
  html, body { width: 1200px; height: 750px; overflow: hidden; }
  body {
    position: relative;
    background: var(--board);
    font-family: "Roboto", Arial, sans-serif;
  }
  .board-caption {
    position: absolute;
    left: 28px;
    top: 56px;
    font-family: "Kreon", Georgia, serif;
    color: var(--white);
  }
  .board-caption .title { font-size: 35px; font-weight: 400; line-height: 32px; }
  .board-caption .subtitle { font-size: 20px; font-weight: 700; line-height: 22px; }
  .board-caption .download {
    margin-top: 26px;
    font-size: 19px;
    line-height: 24px;
    color: var(--accent-text);
  }
  .board-caption .download .link { font-weight: 700; }

  .cover {
    position: absolute;
    left: 519px;
    top: 59px;
    width: 624px;
    height: 624px;
    background: var(--cover-orange);
    box-shadow: 0 4px 18px rgba(0,0,0,0.6);
    overflow: hidden;
  }
  .cover-photo {
    position: absolute;
    left: 0; top: 0;
    width: 624px; height: 397px;
    background:
      linear-gradient(180deg, rgba(150,150,145,0.5) 0%, rgba(255,255,255,0) 30%),
      linear-gradient(90deg, var(--photo-mid) 0%, var(--photo-dark) 20%, var(--photo-mid) 38%, var(--photo-light) 60%, #f3f1ec 100%);
  }
  .cover-tagline {
    position: absolute;
    top: 27px;
    left: 0; width: 624px;
    text-align: center;
    padding-left: 4px;
    font-size: 11px;
    font-weight: 700;
    letter-spacing: 6.2px;
    color: var(--white);
  }
  .cover-title {
    position: absolute;
    right: 30px;
    top: 418px;
    text-align: right;
    color: var(--white);
  }
  .cover-title .city { font-size: 17px; font-weight: 300; letter-spacing: 0.5px; line-height: 20px; }
  .cover-title .headline {
    font-size: 40px;
    font-weight: 900;
    line-height: 36px;
    letter-spacing: -0.5px;
    margin-top: 4px;
  }
  .cover-title .period { font-size: 16px; font-weight: 300; line-height: 22px; margin-top: 2px; }
  .brand {
    position: absolute;
    left: 0; width: 624px;
    top: 574px;
    text-align: center;
    color: var(--white);
  }
  .brand .name { font-size: 17px; font-weight: 900; letter-spacing: -0.3px; line-height: 17px; }
  .brand .descriptor { font-size: 5px; font-weight: 400; letter-spacing: 1px; line-height: 7px; }
</style>
</head>
<body>
  <header class="board-caption">
    <h1 class="title">Brochure</h1>
    <h2 class="subtitle">Cover</h2>
    <p class="download">Full version pdf<br><span class="link">http://files.kestral.eu/r7mPq2Lw</span></p>
  </header>

  <section class="cover">
    <div class="cover-photo" role="img" aria-label="Photo of business people walking through a bright glass-walled office corridor"></div>
    <p class="cover-tagline">The art of seeign the invisible</p>
    <div class="cover-title">
      <p class="city">LUXEMBOURG</p>
      <p class="headline">OFFICE MARKET<br>REPORT</p>
      <p class="period">Q3-2013</p>
    </div>
    <div class="brand">
      <p class="name">KESTRAL</p>
      <p class="descriptor">COMMERCIAL REAL ESTATE</p>
    </div>
  </section>
</body>
</html>
```